Bamboo Toothbrush packaging design

We need a packaging design for a pack of 4 bamboo toothbrushes. The front of the package would need to include the company logo, name of the product - Bamboo Toothbrush, 100% plastic free, and 10% of profit will go to environmental charities . Would like to see some simple or creative graphics to send the message.

Target Market(s)

Retail

Font styles to use
Sans Serif

Colors

Designer to choose colors to be used in the design.

Requirements
Must have
• Just be creative.

```html
<!DOCTYPE html>
<html lang="en">
<head>
<meta charset="utf-8">
<title>Kite Harbor – Bamboo Toothbrush Carton Dieline</title>
<link rel="stylesheet" href="https://fonts.googleapis.com/css2?family=Questrial&display=swap">
<style>
  :root {
    --board: #1d3540;
    --crease: #122830;
    --ink: #ffffff;
    --bamboo-top: #2b4c57;
    --bamboo-bottom: #27444e;
    --paper: #ffffff;
  }
  html, body {
    margin: 0;
    padding: 0;
    width: 1200px;
    height: 2406px;
    overflow: hidden;
    background: var(--paper);
  }
  .dieline {
    display: block;
    width: 1200px;
    height: 2406px;
  }
  .panel, .flap {
    fill: var(--board);
    stroke: var(--crease);
    stroke-width: 1;
  }
  .fold {
    stroke: var(--crease);
    stroke-width: 1;
  }
  .brand-name,
  .product-copy,
  .pledge,
  .imprint {
    font-family: "Questrial", "Century Gothic", sans-serif;
    fill: var(--ink);
  }
  .brand-name { font-size: 44px; font-weight: 400; }
  .product-copy { font-size: 22px; }
  .pledge { font-size: 17px; }
  .imprint { font-size: 12.5px; }
  .pledge-rule { stroke: var(--ink); stroke-width: 2; }
  .brand-dot { fill: var(--ink); }
  .bamboo-art { fill: url(#bambooTone); }
</style>
</head>
<body>
<svg class="dieline" viewBox="0 0 800 1604" xmlns="http://www.w3.org/2000/svg">
  <defs>
    <linearGradient id="bambooTone" x1="0" y1="0" x2="0" y2="1">
      <stop offset="0" stop-color="var(--bamboo-top)" stop-opacity="0.4"/>
      <stop offset="1" stop-color="var(--bamboo-bottom)" stop-opacity="0.9"/>
    </linearGradient>
  </defs>

  <!-- glue flap -->
  <polygon class="flap glue-flap" points="118,266 190,242 190,1362 118,1320"/>

  <!-- top tuck and dust flaps -->
  <path class="flap top-tuck" d="M437,242 V82 Q437,60 459,60 H563 Q585,60 585,82 V242 Z"/>
  <line class="fold" x1="437" y1="145" x2="585" y2="145"/>
  <rect class="flap dust-flap" x="340" y="182" width="93" height="60"/>
  <rect class="flap dust-flap" x="589" y="182" width="94" height="60"/>

  <!-- bottom tuck and dust flaps -->
  <path class="flap bottom-tuck" d="M190,1362 V1523 Q190,1545 212,1545 H318 Q340,1545 340,1523 V1362 Z"/>
  <line class="fold" x1="190" y1="1458" x2="340" y2="1458"/>
  <rect class="flap dust-flap" x="343" y="1362" width="94" height="60"/>
  <rect class="flap dust-flap" x="585" y="1362" width="95" height="60"/>

  <!-- main panels -->
  <rect class="panel front-panel" x="190" y="242" width="150" height="1120"/>
  <rect class="panel side-panel" x="340" y="242" width="97" height="1120"/>
  <rect class="panel back-panel" x="437" y="242" width="148" height="1120"/>
  <rect class="panel side-panel" x="585" y="242" width="98" height="1120"/>

  <!-- bamboo decoration -->
  <rect class="bamboo-art" x="285" y="830" width="115" height="532" role="img" aria-label="Faint bamboo stalks with leaves rising from the base of the front and side panels"/>
  <rect class="bamboo-art" x="510" y="830" width="120" height="532" role="img" aria-label="Faint bamboo stalks with leaves rising from the base of the back and side panels"/>

  <!-- front panel -->
  <g class="brand-lockup">
    <text class="brand-name" transform="translate(212,375) rotate(90)" textLength="290">Kite Harbor</text>
    <circle class="brand-dot" cx="228" cy="682" r="6"/>
  </g>
  <g class="product-copy" transform="translate(258,1022) rotate(90)">
    <text class="product-copy" x="0" y="0">Bamboo Toothbrush</text>
    <text class="product-copy" x="0" y="26">100% plastic free</text>
  </g>

  <!-- side panel -->
  <line class="pledge-rule" x1="370" y1="242" x2="370" y2="730"/>
  <text class="pledge" transform="translate(377,268) rotate(90)" textLength="437">10% of profit will go to environmental charities</text>

  <!-- back panel -->
  <g class="brand-lockup">
    <text class="brand-name" transform="translate(457,375) rotate(90)" textLength="290">Kite Harbor</text>
    <circle class="brand-dot" cx="473" cy="682" r="6"/>
  </g>
  <g transform="translate(498,1022) rotate(90)">
    <text class="product-copy" x="0" y="0">Bamboo Toothbrush</text>
    <text class="product-copy" x="0" y="26">100% plastic free</text>
  </g>

  <!-- imprint side panel -->
  <text class="imprint" transform="translate(627,414) rotate(90)" textLength="318">Made in China  |  Distributed by Kite Harbor</text>
</svg>
</body>
</html>
```